Your conflict - our mediation - joint conflict SOLUTION

With this flyer I am looking for conflict parties who are ready to tackle and resolve their conflict with a prospective mediator. The mediation is free because I am doing it as part of my diploma thesis. Time frame approx. 4 sessions of 2.5 hours each. The wishes and needs of both parties are listened to and “picked out”. In an open, constructive, appreciative framework, solutions are developed and negotiated together.

Target Market(s)

everyone who is ready to deal with himself and his counterpart and everyone who wants to work out a solution with the respect, openness and support of a mediator.

Requirements
Must have
• - "For my diploma thesis I am looking for conflicting parties who are willing to resolve their conflict with a mediator"
- Time frame: 4 x 2.5 hours feasible in Solothurn, Bern, Brugg
- Free of charge
- my coordinates - see business card
- more information at www.talweidenhof.ch
Nice to have
• the card should be based on the style of my homepage www.talweidenhof.ch and my business card

```html
<!DOCTYPE html>
<html lang="de">
<head>
<meta charset="utf-8">
<title>Mediation Flyer</title>
<link href="https://fonts.googleapis.com/css2?family=Open+Sans:ital,wght@0,400;0,600;0,700;1,600&display=swap" rel="stylesheet">
<style>
  :root {
    --page-bg: #633c7b;
    --paper: #f6f5f6;
    --ink-dark: #3d2350;
    --ink-soft: #6e4f84;
    --band-light: #7a5a8b;
    --band-word: #9880a6;
    --band-dark: #3f2651;
    --white: #ffffff;
    --logo-green: #2f7a5a;
  }
  * { margin: 0; padding: 0; box-sizing: border-box; }
  html, body { width: 1070px; height: 1200px; overflow: hidden; }
  body { background: var(--page-bg); font-family: "Open Sans", sans-serif; position: relative; }

  .flyer {
    position: absolute; left: 92px; top: 20px;
    width: 830px; height: 1087px;
    transform: scale(1.0672); transform-origin: top left;
    background: var(--paper); overflow: hidden;
  }
  .headline {
    position: absolute; left: 56px; top: 58px;
    font-size: 49px; line-height: 58px; font-weight: 700; color: var(--ink-dark);
  }
  .brand {
    position: absolute; left: 548px; top: 118px;
    display: flex; align-items: center; gap: 12px;
  }
  .brand-dot { width: 42px; height: 42px; border-radius: 50%; border: 3px solid var(--logo-green); }
  .brand-name { font-size: 32px; font-weight: 600; color: var(--ink-dark); }

  .relations {
    position: absolute; left: 56px; top: 307px; width: 680px;
    font-size: 18.5px; line-height: 23.5px; color: var(--ink-soft);
  }

  .band-light { position: absolute; left: 0; top: 467px; width: 830px; height: 213px; background: var(--band-light); }
  .prompt {
    position: absolute; left: 54px; top: 434px; width: 710px; height: 76px;
    background: var(--ink-dark); border: 2px solid var(--white); border-radius: 38px;
    color: var(--white); font-size: 36px; font-weight: 700;
    display: flex; align-items: center; justify-content: center;
  }
  .word-cloud span { position: absolute; color: var(--band-word); font-weight: 600; white-space: nowrap; }
  .w-sm { font-size: 25px; }
  .w-lg { font-size: 46px; }
  .quote-mark {
    position: absolute; left: 370px; top: 530px;
    font-size: 170px; line-height: 1; font-weight: 700; color: var(--white);
  }

  .band-dark { position: absolute; left: 0; top: 680px; width: 830px; height: 327px; background: var(--band-dark); }
  .appeal {
    position: absolute; left: 0; top: 725px; width: 830px; text-align: center;
    font-size: 26px; line-height: 33px; font-style: italic; font-weight: 600; color: var(--white);
  }
  .point { position: absolute; display: flex; gap: 18px; color: var(--white); font-size: 19.5px; line-height: 24.5px; font-weight: 600; }
  .point-num {
    flex: none; width: 58px; height: 58px; border-radius: 50%; background: var(--white);
    color: var(--ink-dark); font-size: 36px; font-weight: 700;
    display: flex; align-items: center; justify-content: center;
  }
  .point-one { left: 54px; top: 853px; }
  .point-two { left: 546px; top: 850px; align-items: center; }
  .point-one .point-text { margin-top: 2px; }
  .divider { position: absolute; left: 414px; top: 852px; width: 2px; height: 112px; background: var(--white); opacity: .8; }

  .web {
    position: absolute; left: 0; top: 1007px; width: 830px; height: 80px;
    display: flex; align-items: center; justify-content: center;
    font-size: 40px; font-weight: 700; color: var(--ink-dark);
  }
</style>
</head>
<body>
  <main class="flyer">
    <h1 class="headline">Ihr Konflikt -<br>unsere Mediation -<br>gemeinsame<br>KonfliktLÖSUNG</h1>

    <div class="brand">
      <span class="brand-dot"></span>
      <span class="brand-name">Talweidenhof</span>
    </div>

    <p class="relations">mit Ihrer Ehefrau ...  Ihrem Vertragspartner ... Ihrer Nachbarin ... Ihrem Mieter ... Ihrer Tochter ... Ihrem Pächter ... Ihrer Schwester ... Ihrem Geschäftspartner ... Ihrer Vorgesetzten ... Ihrem Mitarbeiter ... Ihrem Vater ... Ihrer Vermieterin ... Ihrem Freund ...</p>

    <div class="band-light"></div>
    <div class="word-cloud" aria-hidden="true">
      <span class="w-sm" style="left:28px;top:536px">mediieren</span>
      <span class="w-lg" style="left:170px;top:515px">klären</span>
      <span class="w-sm" style="left:334px;top:536px">vermitteln</span>
      <span class="w-lg" style="left:488px;top:515px">beraten</span>
      <span class="w-sm" style="left:686px;top:536px">begleiten</span>
      <span class="w-lg" style="left:24px;top:568px">klären</span>
      <span class="w-sm" style="left:191px;top:590px">vermitteln</span>
      <span class="w-lg" style="left:339px;top:568px">beraten</span>
      <span class="w-sm" style="left:537px;top:590px">begleiten</span>
      <span class="w-sm" style="left:676px;top:590px">mediieren</span>
      <span class="w-sm" style="left:22px;top:639px">vermitteln</span>
      <span class="w-lg" style="left:175px;top:618px">beraten</span>
      <span class="w-sm" style="left:375px;top:640px">begleiten</span>
      <span class="w-sm" style="left:516px;top:639px">mediieren</span>
      <span class="w-lg" style="left:664px;top:618px">klären</span>
    </div>
    <div class="quote-mark" aria-hidden="true">“</div>
    <h2 class="prompt">Sie kommen nicht mehr weiter?</h2>

    <div class="band-dark"></div>
    <p class="appeal">For my diploma thesis I am looking for conflicting parties<br>who are willing to resolve their conflict with a mediator</p>

    <div class="point point-one">
      <span class="point-num">1</span>
      <p class="point-text">Time frame:<br>4 x 2.5 hours feasible<br>in Solothurn, Bern,<br>Brugg</p>
    </div>
    <div class="divider"></div>
    <div class="point point-two">
      <span class="point-num">2</span>
      <p class="point-text">Free of charge</p>
    </div>

    <div class="web">www.talweidenhof.ch</div>
  </main>
</body>
</html>
```